Valbrook Data Works

Our company is about IT hardwares and IT solutions. IT hardware such as PC, RAMS, storage and servers. IT solutions such as project management, BA. We are also selling new technology too.

Target Market(s)

Consumer, Small to Medium Business, Corporate

Requirements
Must have
• The business card must have the following:
• Name:
• Title:
• Contact Number:
• Email address:
• Website:
• Color: Must match the logo color upgrade

```html
<!DOCTYPE html>
<html lang="en">
<head>
<meta charset="utf-8">
<title>Valbrook Data Works — Business Card</title>
<link rel="stylesheet" href="https://fonts.googleapis.com/css2?family=Saira:wght@700&family=Open+Sans:wght@400&display=swap">
<style>
  :root {
    --backdrop: #1d1d1f;
    --card: #4a4a4d;
    --card-edge: #3a3a3d;
    --gold: #d29a3c;
    --gold-soft: #b87f2a;
  }
  * { margin: 0; padding: 0; box-sizing: border-box; }
  html, body {
    width: 1200px;
    height: 900px;
    overflow: hidden;
    background: var(--backdrop);
  }
  .stage {
    position: relative;
    width: 1200px;
    height: 900px;
  }
  .card {
    position: absolute;
    width: 560px;
    height: 320px;
    background: var(--card);
    border: 6px solid var(--card-edge);
    border-radius: 6px;
    box-shadow: 0 14px 30px rgba(0,0,0,0.5);
  }
  .card--front { left: 80px; top: 90px; }
  .card--back { left: 560px; top: 490px; }
  .card__frame {
    position: absolute;
    inset: 10px;
    border: 3px solid var(--gold);
    border-radius: 4px;
    display: flex;
    flex-direction: column;
    align-items: center;
    justify-content: center;
  }
  .brand {
    display: flex;
    flex-direction: column;
    align-items: center;
    gap: 12px;
  }
  .brand__dot {
    width: 40px;
    height: 40px;
    border-radius: 50%;
    background: var(--gold);
    flex: none;
  }
  .brand__name {
    font-family: "Saira", sans-serif;
    font-weight: 700;
    text-transform: uppercase;
    color: var(--gold);
    font-size: 40px;
    line-height: 1.05;
    letter-spacing: 1px;
    text-align: center;
  }
  .brand__line { display: block; }
  .card--back .card__frame { justify-content: flex-start; padding-top: 30px; }
  .card--back .brand { gap: 8px; }
  .card--back .brand__dot { width: 24px; height: 24px; }
  .card--back .brand__name { font-size: 26px; }
  .contact {
    margin-top: 14px;
    list-style: none;
    text-align: center;
    font-family: "Open Sans", sans-serif;
    font-size: 15px;
    line-height: 1.3;
    color: var(--gold-soft);
  }
</style>
</head>
<body>
<main class="stage">
  <section class="card card--front" aria-label="Card front">
    <div class="card__frame">
      <div class="brand">
        <span class="brand__dot"></span>
        <span class="brand__name"><span class="brand__line">Valbrook Data</span><span class="brand__line">Works</span></span>
      </div>
    </div>
  </section>

  <section class="card card--back" aria-label="Card back">
    <div class="card__frame">
      <div class="brand">
        <span class="brand__dot"></span>
        <span class="brand__name"><span class="brand__line">Valbrook Data</span><span class="brand__line">Works</span></span>
      </div>
      <ul class="contact">
        <li>Name</li>
        <li>Title</li>
        <li>Contact Number</li>
        <li>Email address</li>
        <li>Website</li>
      </ul>
    </div>
  </section>
</main>
</body>
</html>
```